Land Buying Company Needs Letterhead for Direct Mail Marketing to Land Owners

We are looking for a professional letterhead that we will be including in our direct mail marketing. We will be sending this to land owners who may be interested in selling or purchasing land.

The letterhead needs to be editable. Headers and footers would look nice, but we are open. We would want it to include our address, website, phone, and email info. For right now the address to use for design purposes would the following:

Address: 412 Fenwick Avenue #300
Dallas, TX 75319
Website - www.quillbrookacres.com
Email - info@quillbrookacres.com
Phone - 866-492-ACRE

I have attached our logo zip file that we just had done on Pixel Harbor. Let me know what questions you have, and thank you.

```html
<!DOCTYPE html>
<html lang="en">
<head>
<meta charset="utf-8">
<title>Quillbrook Acres Letterhead</title>
<link href="https://fonts.googleapis.com/css2?family=Lato:wght@400&family=Montserrat:wght@700&display=swap" rel="stylesheet">
<style>
  :root {
    --backdrop: #9a9a9a;
    --paper: #e3e3e3;
    --leaf: #9acd3c;
    --forest: #46601f;
    --charcoal: #231f20;
    --steel-dark: #7a7a7a;
    --steel-light: #d4d4d4;
    --ink-light: #f2f2f2;
  }
  html, body {
    margin: 0;
    padding: 0;
    width: 1200px;
    height: 1145px;
    overflow: hidden;
    background: var(--backdrop);
  }
  .letterhead {
    position: absolute;
    left: 175px;
    top: 22px;
    width: 850px;
    height: 1100px;
    background: var(--paper);
    overflow: hidden;
  }
  .brand {
    position: absolute;
    left: 51px;
    top: 64px;
    display: flex;
    align-items: center;
    gap: 20px;
  }
  .brand-dot {
    width: 84px;
    height: 84px;
    border-radius: 50%;
    background: var(--forest);
  }
  .brand-name {
    font-family: "Montserrat", sans-serif;
    font-weight: 700;
    font-size: 34px;
    letter-spacing: 2px;
    color: var(--leaf);
    text-transform: uppercase;
  }
  .footer {
    position: absolute;
    left: 0;
    top: 1019px;
    width: 850px;
    height: 70px;
  }
  .rule {
    position: absolute;
    left: 0;
    width: 600px;
    height: 8px;
    background: linear-gradient(90deg, var(--steel-dark), var(--steel-light) 50%, var(--steel-dark));
  }
  .rule-top { top: 0; }
  .rule-bottom { top: 63px; }
  .contact-band {
    position: absolute;
    left: 0;
    top: 12px;
    width: 600px;
    height: 46px;
    background: var(--forest);
    display: flex;
    align-items: center;
    gap: 14px;
    padding-left: 25px;
    box-sizing: border-box;
    font-family: "Lato", sans-serif;
    font-size: 12.5px;
    color: var(--ink-light);
  }
  .contact-item {
    display: flex;
    align-items: center;
    gap: 5px;
    white-space: nowrap;
  }
  .contact-item svg { flex: none; }
  .contact-web { margin-left: 6px; }
  .address-block {
    position: absolute;
    left: 652px;
    top: 0;
    width: 198px;
    height: 67px;
    background: var(--charcoal);
    box-sizing: border-box;
    padding: 12px 0 0 26px;
    font-family: "Lato", sans-serif;
    font-size: 15.5px;
    line-height: 20px;
    color: var(--ink-light);
  }
  .footer-dot {
    position: absolute;
    left: 576px;
    top: -12px;
    width: 78px;
    height: 78px;
    border-radius: 50%;
    background: var(--forest);
    border: 8px solid var(--paper);
  }
</style>
</head>
<body>
  <main class="letterhead">
    <header class="brand">
      <div class="brand-dot"></div>
      <div class="brand-name">Quillbrook Acres</div>
    </header>

    <footer class="footer">
      <div class="rule rule-top"></div>
      <div class="contact-band">
        <span class="contact-item">
          <svg width="13" height="13" viewBox="0 0 16 16" aria-hidden="true">
            <circle cx="8" cy="8" r="7" fill="none" stroke="currentColor" stroke-width="1.3"/>
            <path d="M5.3 4.3l1.4 1.5-.8 1a5 5 0 0 0 2.3 2.3l1-.8 1.5 1.4-.9 1.2c-2.8-.3-5.4-2.9-5.7-5.7z" fill="currentColor"/>
          </svg>
          866-492-ACRE
        </span>
        <span class="contact-item">
          <svg width="14" height="11" viewBox="0 0 14 11" aria-hidden="true">
            <rect x="0.6" y="0.6" width="12.8" height="9.8" fill="none" stroke="currentColor" stroke-width="1.1"/>
            <path d="M0.6 0.8L7 6l6.4-5.2" fill="none" stroke="currentColor" stroke-width="1.1"/>
          </svg>
          info@quillbrookacres.com
        </span>
        <span class="contact-item contact-web">
          <svg width="16" height="16" viewBox="0 0 16 16" aria-hidden="true">
            <circle cx="8" cy="8" r="7" fill="none" stroke="currentColor" stroke-width="1.3"/>
            <ellipse cx="8" cy="8" rx="3" ry="7" fill="none" stroke="currentColor" stroke-width="1"/>
            <path d="M1 8h14M2.2 4.5h11.6M2.2 11.5h11.6" stroke="currentColor" stroke-width="1"/>
          </svg>
          &nbsp;www.quillbrookacres.com
        </span>
      </div>
      <div class="rule rule-bottom"></div>
      <address class="address-block" style="font-style: normal;">
        412 Fenwick Avenue<br>
        #300 Dallas, TX 75319
      </address>
      <div class="footer-dot"></div>
    </footer>
  </main>
</body>
</html>
```